Copperline Ridge Footraces

We need a website (wordpress) design for a new website that we will be launching. This is for a new trail racing series in Canada.
We recently had a logo designed so want to incorporate the colours of the logo on the website design. Especially the dark blue, green and orange.
Websites that we like for comparison of trail running race themes are:
https://www.brambleroutefest.com/
https://www.stridecolmcircuit.com/
http://www.fernpathcircuit.ca/
https://www.silvanloopcircuit.com/
http://www.marbrookrunlineup.com/

Target Market(s)

Outdoor trail runners

Coding

Coded - Design and coding required

Number of Pages Required

4 page

Font styles to use
Sans Serif

Colors
0255a3
33b8a4
f37122

Requirements
Must have
• There will be a main page with eye catching design noting what we do. Page 2 and 3 will be for each race in the series. Page 1 will be a specific race, and page 2 with be for another race. page 3 and 4 will be for future races that we add so that each race has their own page.
• Our races all take place in the mountains, so using graphics including mountains, rivers, trees is all a requirement for us.
• Our logo is attached, we want to use the colours of the logo in the website design.
Nice to have
• Outdoor theme is a nice to have. We like wood and earth tone colours, and pictures/graphics of runners and mountains and trees.
• There are 4 people involved in our organization. We'd like a photo and brief blurb of each of us, similar to how this website did their layout: https://www.brambleroutefest.com/

```html
<!DOCTYPE html>
<html lang="en">
<head>
<meta charset="utf-8">
<title>Copperline Ridge Footraces</title>
<link href="https://fonts.googleapis.com/css2?family=Roboto+Condensed:wght@400;700&family=Lato:wght@400;700&display=swap" rel="stylesheet">
<style>
:root{
  --blue:#0255a3;
  --teal:#33b8a4;
  --orange:#f37122;
  --ink:#4a4a4a;
  --light:#f2f2f2;
  --footer:#1b1b1b;
  --white:#ffffff;
}
*{box-sizing:border-box;margin:0;padding:0}
html,body{width:1200px;height:4800px;overflow:hidden}
body{font-family:"Lato",sans-serif;color:var(--ink);background:var(--white);font-size:15px;line-height:1.6}
h1,h2,h3,.nav a,.btn{font-family:"Roboto Condensed",sans-serif;font-weight:700;text-transform:uppercase}
.btn{display:inline-block;color:var(--white);font-size:14px;letter-spacing:.5px;text-align:center;line-height:48px;height:48px}
.btn-teal{background:var(--teal);width:180px}
.btn-orange{background:var(--orange)}
.more{font-family:"Lato",sans-serif;font-size:13px;font-weight:700;color:var(--orange);text-transform:uppercase;display:inline-flex;align-items:center;gap:5px}
.more svg{width:13px;height:13px}
.section-title{font-size:50px;color:var(--blue);text-align:center;letter-spacing:.3px;line-height:1.15}
.photo{display:block}

/* Hero */
.hero{position:relative;height:662px;overflow:hidden}
.hero-bg{position:absolute;inset:0;background:
  radial-gradient(ellipse 520px 300px at 78% 28%,rgba(236,214,160,.55),rgba(236,214,160,0) 70%),
  radial-gradient(ellipse 600px 260px at 15% 85%,rgba(60,40,28,.7),rgba(60,40,28,0) 70%),
  linear-gradient(180deg,#8c9a74 0%,#5f7048 30%,#4b5236 55%,#6b5a40 78%,#3a2e24 100%)}
.hero-shade{position:absolute;inset:0;background:rgba(0,0,0,.28)}
.brand{position:absolute;left:78px;top:30px;width:112px;text-align:center;color:var(--white)}
.brand-dot{width:46px;height:46px;border-radius:50%;background:var(--orange);margin:0 auto 8px}
.brand-name{font-family:"Roboto Condensed",sans-serif;font-weight:700;font-size:20px;line-height:1.05;text-transform:uppercase}
.nav{position:absolute;top:88px;left:390px;display:flex;gap:38px}
.nav a{color:var(--white);font-size:14px;text-decoration:none}
.nav a.active{color:var(--orange)}
.hero h1{position:absolute;top:300px;left:0;right:0;text-align:center;color:var(--white);font-size:60px;letter-spacing:0;transform:scaleX(.88)}
.hero .btn{position:absolute;top:408px;left:498px;width:206px;display:flex;align-items:center;justify-content:center;gap:10px}
.hero .btn svg{width:18px;height:18px}
.arrow{position:absolute;top:375px;width:24px;height:40px}
.arrow.left{left:60px}.arrow.right{right:60px}

/* Welcome */
.welcome{height:413px;padding-top:58px;text-align:center}
.welcome p{width:880px;margin:22px auto 30px;font-size:15px;line-height:1.75}

/* Upcoming */
.upcoming{position:relative;height:712px}
.upcoming-bg{position:absolute;inset:0;background:
  radial-gradient(ellipse 500px 200px at 85% 10%,rgba(220,230,240,.5),rgba(220,230,240,0) 70%),
  linear-gradient(180deg,#7e8c98 0%,#5c6770 22%,#4d5550 45%,#3e4b3c 62%,#2f5a63 80%,#3d4440 92%,#5a5a55 100%)}
.upcoming-shade{position:absolute;inset:0;background:rgba(0,0,0,.15)}
.upcoming .section-title{position:relative;color:var(--white);padding-top:52px}
.race-cards{position:relative;display:flex;gap:30px;margin:28px 0 0 75px}
.race-card{width:330px;background:var(--white);text-align:center}
.race-card .photo{height:238px}
.race-card h3{color:var(--teal);font-size:24px;margin-top:18px}
.race-card p{font-size:13px;line-height:1.55;margin:8px 34px 12px}
.dots{position:relative;display:flex;gap:10px;justify-content:center;margin-top:66px}
.dots span{width:26px;height:3px;background:rgba(255,255,255,.5)}
.dots span.on{background:var(--white)}

/* Features */
.feature{display:flex;gap:30px;padding:0 75px}
.feature .photo{width:510px;height:314px;flex:none}
.feature-text{width:510px}
.feature h2{font-size:52px;color:var(--blue);line-height:1.1}
.feature p{font-size:15px;margin:18px 0 30px;line-height:1.7}
.about{height:455px;padding-top:73px}
.about .feature-text{padding-top:10px}
.rules{height:385px;padding-top:0}
.rules .feature-text{padding-top:25px}

/* Team */
.team{position:relative;height:720px}
.team-bg{position:absolute;inset:0;background:
  radial-gradient(ellipse 200px 500px at 50% 30%,rgba(150,170,120,.35),rgba(150,170,120,0) 70%),
  radial-gradient(ellipse 160px 500px at 12% 40%,rgba(130,150,100,.3),rgba(130,150,100,0) 70%),
  radial-gradient(ellipse 160px 500px at 90% 40%,rgba(130,150,100,.3),rgba(130,150,100,0) 70%),
  linear-gradient(180deg,#2e3f26 0%,#1f2d1a 50%,#34422a 100%)}
.team .section-title{position:relative;color:var(--white);padding-top:52px}
.team-grid{position:relative;display:grid;grid-template-columns:510px 510px;gap:30px;margin:24px 0 0 75px}
.member{display:flex;height:235px;background:var(--white)}
.member-text{width:270px;padding:22px 22px}
.member h3{color:var(--teal);font-size:22px}
.member p{font-size:13px;line-height:1.55;margin:6px 0 8px}
.member .photo{width:240px;height:235px}

/* Sponsors */
.sponsors{height:300px;padding-top:60px}
.sponsors .section-title{font-size:34px}
.sponsor-row{display:flex;justify-content:space-between;align-items:center;width:920px;margin:55px auto 0}
.sponsor{font-family:"Roboto Condensed",sans-serif;font-weight:700;font-size:22px;color:#5a4632;text-transform:uppercase;display:flex;align-items:center;gap:10px}
.sponsor .mark{width:60px;height:60px;border-radius:50%;background:#c8372d}
.sponsor .sq{width:20px;height:20px;background:#c8372d}

/* Blog */
.blog{height:585px;background:var(--light);padding-top:62px}
.blog-row{display:flex;gap:30px;margin:30px 0 0 75px}
.post{width:330px;text-align:center}
.post .photo{height:200px}
.post h3{color:var(--teal);font-size:24px;margin-top:30px}
.post p{font-size:13px;line-height:1.55;margin:6px 20px 16px}

/* Instagram */
.insta{height:300px;padding-top:45px}
.insta .section-title{font-size:34px}
.insta-row{display:flex;gap:18px;margin:22px 0 0 75px}
.insta-row .photo{width:252px;height:172px}

/* Footer */
.footer{height:275px;background:var(--footer);color:#bdbdbd;position:relative}
.footer-brand{position:absolute;left:78px;top:50px;width:112px;color:var(--white);text-align:center}
.footer-copy{position:absolute;left:78px;top:205px;font-size:11px;line-height:1.5;color:#9a9a9a}
.footer h3{color:var(--teal);font-size:18px}
.sitemap{position:absolute;left:342px;top:48px}
.sitemap-cols{display:flex;gap:70px;margin-top:8px;font-size:12px;line-height:1.8;color:#cfcfcf}
.subscribe{position:absolute;left:615px;top:48px}
.field{width:240px;height:40px;background:var(--white);color:#555;font-size:12px;line-height:40px;padding-left:12px;margin-top:14px}
.subscribe .btn{width:92px;height:40px;line-height:40px;font-size:13px;margin:12px 0 0 152px}
.follow{position:absolute;left:910px;top:48px}
.social{display:flex;gap:14px;margin-top:16px}
.social span{width:22px;height:22px;border-radius:50%;border:2px solid #cfcfcf}
</style>
</head>
<body>

<header class="hero">
  <div class="hero-bg" role="img" aria-label="Trail runners racing along a sunlit forest path in the mountains"></div>
  <div class="hero-shade"></div>
  <div class="brand">
    <div class="brand-dot"></div>
    <div class="brand-name">Copperline Ridge</div>
  </div>
  <nav class="nav">
    <a class="active">Home</a><a>About</a><a>Races</a><a>Media</a><a>Results</a><a>Store</a><a>Blog</a><a>Contact Us</a>
  </nav>
  <svg class="arrow left" viewBox="0 0 24 40"><path d="M20 3 4 20l16 17" fill="none" stroke="#fff" stroke-width="3"/></svg>
  <svg class="arrow right" viewBox="0 0 24 40"><path d="M4 3l16 17L4 37" fill="none" stroke="#fff" stroke-width="3"/></svg>
  <h1>Are you ready for race?</h1>
  <a class="btn btn-orange"><svg viewBox="0 0 18 18"><circle cx="9" cy="9" r="8" fill="#fff"/><path d="M7 5.5v7l5.5-3.5z" fill="#f37122"/></svg>Watch a video</a>
</header>

<section class="welcome">
  <h2 class="section-title">Welcome to our website</h2>
  <p>Lorem ipsum dolor sit amet, consectetur adipiscing elit. Aenean interdum, justo eget ullamcorper feugiat, magna sapien auctor magna, eget iaculis dui arcu congue risus. Maecenas tempus mattis sagittis. Integer lobortis ex nunc, ut luctus mauris congue a. Quisque tincidunt orci vitae sapien varius, nec imperdiet erat tincidunt. Suspendisse ultricies, mauris et viverra sagittis, arcu odio luctus massa, ac sagittis sapien velit nibh et justo.</p>
  <a class="btn btn-teal">Read more</a>
</section>

<section class="upcoming">
  <div class="upcoming-bg" role="img" aria-label="Mountain lake framed by rocky peaks and pine forest"></div>
  <div class="upcoming-shade"></div>
  <h2 class="section-title">Upcoming race</h2>
  <div class="race-cards">
    <article class="race-card">
      <div class="photo" role="img" aria-label="Runners on a shaded forest trail" style="background:radial-gradient(ellipse 120px 90px at 60% 35%,rgba(170,190,120,.5),rgba(170,190,120,0) 70%),linear-gradient(180deg,#4f6a3a 0%,#2f4a26 50%,#3a3526 80%,#2a2620 100%)"></div>
      <h3>Aug 15, 2018</h3>
      <p>Vestibulum ante ipsum primis in faucibus orci luctus et ultrices iaculis.</p>
      <a class="more">More info <svg viewBox="0 0 13 13"><circle cx="6.5" cy="6.5" r="6.5" fill="#f37122"/><path d="M5 3.5 8 6.5 5 9.5" fill="none" stroke="#fff" stroke-width="1.6"/></svg></a>
    </article>
    <article class="race-card">
      <div class="photo" role="img" aria-label="Group of runners climbing a dirt trail through trees" style="background:linear-gradient(180deg,#6b7a4a 0%,#55603a 35%,#9a8260 60%,#b99a70 80%,#7a6448 100%)"></div>
      <h3>Aug 15, 2018</h3>
      <p>Vestibulum ante ipsum primis in faucibus orci luctus et ultrices iaculis.</p>
      <a class="more">More info <svg viewBox="0 0 13 13"><circle cx="6.5" cy="6.5" r="6.5" fill="#f37122"/><path d="M5 3.5 8 6.5 5 9.5" fill="none" stroke="#fff" stroke-width="1.6"/></svg></a>
    </article>
    <article class="race-card">
      <div class="photo" role="img" aria-label="Runners on a sunny mountain trail below blue sky" style="background:linear-gradient(180deg,#7fb4e0 0%,#a9cbe6 22%,#8f9a8a 38%,#4f6b3e 55%,#a88460 78%,#c9a57a 100%)"></div>
      <h3>Aug 15, 2018</h3>
      <p>Vestibulum ante ipsum primis in faucibus orci luctus et ultrices iaculis.</p>
      <a class="more">More info <svg viewBox="0 0 13 13"><circle cx="6.5" cy="6.5" r="6.5" fill="#f37122"/><path d="M5 3.5 8 6.5 5 9.5" fill="none" stroke="#fff" stroke-width="1.6"/></svg></a>
    </article>
  </div>
  <div class="dots"><span class="on"></span><span></span><span class="on"></span><span class="on"></span></div>
</section>

<section class="feature about">
  <div class="photo" role="img" aria-label="Three trail runners in a sunlit forest" style="background:radial-gradient(ellipse 260px 180px at 20% 20%,rgba(240,225,190,.8),rgba(240,225,190,0) 70%),linear-gradient(160deg,#c8b48a 0%,#8d8460 40%,#5e6440 70%,#3e4a2c 100%)"></div>
  <div class="feature-text">
    <h2>About races</h2>
    <p>Aliquam molestie, mi et imperdiet euismod, dui purus auctor tellus, et interdum lacus lectus et ante. Sed accumsan sollicitudin sapien, sit amet adipiscing turpis gravida ac. In congue, neque ac lobortis volutpat, libero mauris varius mi.</p>
    <a class="btn btn-teal">Read more</a>
  </div>
</section>

<section class="feature rules">
  <div class="feature-text">
    <h2>Rules &amp; results</h2>
    <p>Aliquam molestie, mi et imperdiet euismod, dui purus auctor tellus, et interdum lacus lectus et ante. Sed accumsan sollicitudin sapien, sit amet adipiscing turpis gravida ac. In congue, neque ac lobortis volutpat, libero mauris varius mi.</p>
    <a class="btn btn-teal">View results</a>
  </div>
  <div class="photo" role="img" aria-label="Runners on a dry hillside trail" style="background:radial-gradient(ellipse 200px 140px at 40% 60%,rgba(200,170,120,.6),rgba(200,170,120,0) 70%),linear-gradient(160deg,#5c6a3a 0%,#8b7a52 40%,#a08660 65%,#4d5530 100%)"></div>
</section>

<section class="team">
  <div class="team-bg" role="img" aria-label="Dense pine forest with light between the trunks"></div>
  <h2 class="section-title">Our team</h2>
  <div class="team-grid">
    <article class="member">
      <div class="member-text"><h3>Name heading</h3><p>Vestibulum ante ipsum primis in faucibus orci luctus et ultrices iaculis scelerisque rhoncus sapien ac ultrices. Nullam tempor sed risus sed laoreet..</p>
      <a class="more">More info <svg viewBox="0 0 13 13"><circle cx="6.5" cy="6.5" r="6.5" fill="#f37122"/><path d="M5 3.5 8 6.5 5 9.5" fill="none" stroke="#fff" stroke-width="1.6"/></svg></a></div>
      <div class="photo" role="img" aria-label="Portrait of a team member outdoors" style="background:linear-gradient(180deg,#a9bfcc 0%,#8aa0ae 45%,#b89a86 70%,#6d8493 100%)"></div>
    </article>
    <article class="member">
      <div class="photo" role="img" aria-label="Portrait of a team member in a blue top" style="background:linear-gradient(180deg,#e0e6ea 0%,#c9d3da 40%,#3f79b8 75%,#2a5f9a 100%)"></div>
      <div class="member-text"><h3>Name heading</h3><p>Vestibulum ante ipsum primis in faucibus orci luctus et ultrices iaculis scelerisque rhoncus sapien ac ultrices. Nullam tempor sed risus sed laoreet..</p>
      <a class="more">More info <svg viewBox="0 0 13 13"><circle cx="6.5" cy="6.5" r="6.5" fill="#f37122"/><path d="M5 3.5 8 6.5 5 9.5" fill="none" stroke="#fff" stroke-width="1.6"/></svg></a></div>
    </article>
    <article class="member">
      <div class="member-text"><h3>Name heading</h3><p>Vestibulum ante ipsum primis in faucibus orci luctus et ultrices iaculis scelerisque rhoncus sapien ac ultrices. Nullam tempor sed risus sed laoreet..</p>
      <a class="more">More info <svg viewBox="0 0 13 13"><circle cx="6.5" cy="6.5" r="6.5" fill="#f37122"/><path d="M5 3.5 8 6.5 5 9.5" fill="none" stroke="#fff" stroke-width="1.6"/></svg></a></div>
      <div class="photo" role="img" aria-label="Portrait of a team member with a towel" style="background:linear-gradient(180deg,#eeece8 0%,#d9d3c8 45%,#c9b8a6 75%,#b0a898 100%)"></div>
    </article>
    <article class="member">
      <div class="photo" role="img" aria-label="Portrait of a team member at the finish area" style="background:linear-gradient(180deg,#9fb3c0 0%,#6f8595 40%,#2f4f6f 75%,#22384e 100%)"></div>
      <div class="member-text"><h3>Name heading</h3><p>Vestibulum ante ipsum primis in faucibus orci luctus et ultrices iaculis scelerisque rhoncus sapien ac ultrices. Nullam tempor sed risus sed laoreet..</p>
      <a class="more">More info <svg viewBox="0 0 13 13"><circle cx="6.5" cy="6.5" r="6.5" fill="#f37122"/><path d="M5 3.5 8 6.5 5 9.5" fill="none" stroke="#fff" stroke-width="1.6"/></svg></a></div>
    </article>
  </div>
</section>

<section class="sponsors">
  <h2 class="section-title">Sponsors</h2>
  <div class="sponsor-row">
    <div class="sponsor"><span class="sq" style="background:#8a6a3c"></span>Harrowgate Lodge</div>
    <div class="sponsor"><span class="mark" role="img" aria-label="Partner badge"></span></div>
    <div class="sponsor" style="color:#2f4a3a">Tallis Gorge Outdoors</div>
    <div class="sponsor" style="color:#c8372d"><span class="sq"></span>Brisk Fuel Co.</div>
  </div>
</section>

<section class="blog">
  <h2 class="section-title">Blog</h2>
  <div class="blog-row">
    <article class="post">
      <div class="photo" role="img" aria-label="Runners on a green forest trail" style="background:linear-gradient(180deg,#6f9a48 0%,#4a7a32 40%,#335e26 70%,#6b5a3a 100%)"></div>
      <h3>Lorem ipsum dolor sit amet</h3>
      <p>Vestibulum ante ipsum primis in faucibus orci luctus et ultrices iaculis nibh eget turpis vehicula tempus ac sed..</p>
      <a class="more">More info <svg viewBox="0 0 13 13"><circle cx="6.5" cy="6.5" r="6.5" fill="#f37122"/><path d="M5 3.5 8 6.5 5 9.5" fill="none" stroke="#fff" stroke-width="1.6"/></svg></a>
    </article>
    <article class="post">
      <div class="photo" role="img" aria-label="Runner crossing a sandy canyon by the sea" style="background:linear-gradient(180deg,#7fb0c8 0%,#c9a070 30%,#dba878 60%,#a36a3c 100%)"></div>
      <h3>Lorem ipsum dolor sit amet</h3>
      <p>Vestibulum ante ipsum primis in faucibus orci luctus et ultrices iaculis nibh eget turpis vehicula tempus ac sed..</p>
      <a class="more">More info <svg viewBox="0 0 13 13"><circle cx="6.5" cy="6.5" r="6.5" fill="#f37122"/><path d="M5 3.5 8 6.5 5 9.5" fill="none" stroke="#fff" stroke-width="1.6"/></svg></a>
    </article>
    <article class="post">
      <div class="photo" role="img" aria-label="Runners below snowy mountain peaks" style="background:linear-gradient(180deg,#6fa2d6 0%,#a9c4dc 25%,#eef2f4 42%,#8a9aa0 58%,#5f7a4a 80%,#7a6a4a 100%)"></div>
      <h3>Lorem ipsum dolor sit amet</h3>
      <p>Vestibulum ante ipsum primis in faucibus orci luctus et ultrices iaculis nibh eget turpis vehicula tempus ac sed..</p>
      <a class="more">More info <svg viewBox="0 0 13 13"><circle cx="6.5" cy="6.5" r="6.5" fill="#f37122"/><path d="M5 3.5 8 6.5 5 9.5" fill="none" stroke="#fff" stroke-width="1.6"/></svg></a>
    </article>
  </div>
</section>

<section class="insta">
  <h2 class="section-title">Instagram</h2>
  <div class="insta-row">
    <div class="photo" role="img" aria-label="Runners on a shaded trail" style="background:linear-gradient(180deg,#5d7a48 0%,#34502a 50%,#26381f 100%)"></div>
    <div class="photo" role="img" aria-label="Runners in race gear on a road" style="background:linear-gradient(180deg,#b7cadb 0%,#7d96a8 45%,#5a6f7d 100%)"></div>
    <div class="photo" role="img" aria-label="Group of runners at sunset" style="background:radial-gradient(ellipse 140px 90px at 30% 25%,rgba(255,225,160,.8),rgba(255,225,160,0) 70%),linear-gradient(180deg,#e7b77a 0%,#b5824e 55%,#6a4630 100%)"></div>
    <div class="photo" role="img" aria-label="Runners on a trail in warm light" style="background:linear-gradient(180deg,#d6ae80 0%,#a77a54 50%,#6d4b33 100%)"></div>
  </div>
</section>

<footer class="footer">
  <div class="footer-brand">
    <div class="brand-dot"></div>
    <div class="brand-name">Copperline Ridge</div>
  </div>
  <div class="footer-copy">Copyright © 2018. Company Name<br>All Right Reserved</div>
  <div class="sitemap">
    <h3>Site map</h3>
    <div class="sitemap-cols">
      <div>Home<br>About<br>Races<br>Media<br>Results</div>
      <div>Store<br>Blog<br>Contact Us</div>
    </div>
  </div>
  <div class="subscribe">
    <h3>Email subscribe</h3>
    <div class="field">Enter Email Address</div>
    <a class="btn btn-orange">Sign up</a>
  </div>
  <div class="follow">
    <h3>Follow us</h3>
    <div class="social"><span></span><span></span><span></span></div>
  </div>
</footer>

</body>
</html>
```